Business card design for new, innovative company - BoldHarbor

We are a new company looking for a business card design that is fun, different and quirky. Must use corporate colour green - CMYK C:55, M:0, Y:100, K:0, and corporate colour grey - C:0, M:0, Y: 0, K:70.

We have developed the first real time data application, in which people are able to profile the data of their existing customers in order to pull out more good fit clients to direct their marketing activities at.

Industry/Entity Type

Marketing

Requirements
Must have
• Logo, name, title, telephone number, fax number, email, website, address

```html
<!DOCTYPE html>
<html lang="en">
<head>
<meta charset="utf-8">
<title>BoldHarbor Business Card</title>
<link rel="stylesheet" href="https://fonts.googleapis.com/css2?family=Jost:wght@400;500;700&display=swap">
<style>
  :root {
    --brand-green: #7dc242;
    --brand-grey: #6d6e70;
    --card-white: #f1f1f1;
    --page-bg: #dcdad6;
    --text-white: #ffffff;
  }
  * { box-sizing: border-box; margin: 0; padding: 0; }
  html, body { width: 1200px; height: 720px; overflow: hidden; }
  body {
    background: var(--page-bg);
    font-family: "Jost", sans-serif;
    position: relative;
  }
  .card {
    position: absolute;
    top: 212px;
    width: 520px;
    height: 297px;
    border-radius: 3px;
    box-shadow: 0 4px 14px rgba(0,0,0,0.18);
    overflow: hidden;
  }
  .card-front { left: 50px; background: var(--card-white); }
  .card-back { left: 630px; background: var(--brand-green); }

  .wordmark {
    position: absolute;
    left: 0; right: 0;
    display: flex;
    justify-content: center;
    align-items: center;
    gap: 10px;
    font-weight: 700;
    letter-spacing: -0.5px;
    line-height: 1;
  }
  .wordmark-square {
    width: 14px;
    height: 14px;
    flex: none;
  }
  .card-front .wordmark { top: 52px; font-size: 46px; color: var(--brand-green); }
  .card-front .wordmark-square { background: var(--brand-grey); }
  .card-back .wordmark { top: 100px; font-size: 50px; color: var(--text-white); }
  .card-back .wordmark-square { background: var(--text-white); }

  .website {
    position: absolute;
    top: 168px; left: 0; right: 0;
    text-align: center;
    font-size: 13px;
    color: var(--text-white);
    letter-spacing: 0.3px;
  }

  .name-band {
    position: absolute;
    top: 150px; left: 0;
    width: 212px; height: 30px;
    background: var(--brand-green);
    color: var(--text-white);
    font-size: 19px;
    font-weight: 500;
    line-height: 30px;
    padding-left: 30px;
  }

  .contact-list {
    position: absolute;
    top: 192px; left: 30px;
    list-style: none;
    color: var(--brand-grey);
    font-size: 15px;
    line-height: 21px;
    letter-spacing: 0.3px;
  }
  .contact-list li { display: flex; align-items: center; gap: 10px; }
  .contact-list svg { width: 11px; height: 11px; fill: var(--brand-green); flex: none; }

  .address {
    position: absolute;
    top: 146px; right: 46px;
    text-align: right;
    color: var(--brand-grey);
    font-size: 15px;
    line-height: 19px;
    font-style: normal;
    letter-spacing: 0.3px;
  }
  .address-pin {
    position: absolute;
    top: 148px; right: 26px;
    width: 11px; height: 15px;
    fill: var(--brand-green);
  }
</style>
</head>
<body>

<section class="card card-front" aria-label="Card front">
  <div class="wordmark"><span>BoldHarbor</span><span class="wordmark-square" aria-hidden="true"></span></div>

  <div class="name-band">Jenna Corwin</div>

  <ul class="contact-list">
    <li>
      <svg viewBox="0 0 12 12" aria-hidden="true"><path d="M1 4 Q6 0 11 4 L9 5.5 L7.5 4.5 L4.5 4.5 L3 5.5 Z M3 6.5 H9 L10 11 H2 Z"/></svg>
      07700900184
    </li>
    <li>
      <svg viewBox="0 0 12 12" aria-hidden="true"><rect x="3" y="0.5" width="6" height="11" rx="1.2"/></svg>
      01632 960418
    </li>
    <li>
      <svg viewBox="0 0 12 12" aria-hidden="true"><path d="M0.5 2.5 H11.5 V9.5 H0.5 Z M1 3 L6 7 L11 3" stroke="#f1f1f1" stroke-width="0.8"/></svg>
      jenna.corwin@boldharbor.com
    </li>
  </ul>

  <address class="address">22a Fenmill Road,<br>Elmsby, Northshire,<br>NE27 4QT</address>
  <svg class="address-pin" viewBox="0 0 11 15" aria-hidden="true"><path d="M5.5 0 A5.5 5.5 0 0 1 11 5.5 C11 9 5.5 15 5.5 15 C5.5 15 0 9 0 5.5 A5.5 5.5 0 0 1 5.5 0 Z M5.5 3.5 A2 2 0 1 0 5.5 7.5 A2 2 0 1 0 5.5 3.5 Z"/></svg>
</section>

<section class="card card-back" aria-label="Card back">
  <div class="wordmark"><span>BoldHarbor</span><span class="wordmark-square" aria-hidden="true"></span></div>
  <div class="website">www.boldharbor.com</div>
</section>

</body>
</html>
```